homepage design , industry automation control image

we need a design , based on our Logo image.

we focus on selling of temprature sensor ,and parts.

but need concept or image on industry automation control

we need enviroment friendly concept.

Industry/Entity Type

Industry

Number of Pages Required

5+ page

Requirements
Must have
• we need a Cartoon Image of a Temperature sensor,
• attaching a Excel file with the sensor looking.
Nice to have
• Nature image, future concept

```html
<!DOCTYPE html>
<html lang="en">
<head>
<meta charset="utf-8">
<title>Lindqvist Messtechnik</title>
<link href="https://fonts.googleapis.com/css2?family=Oswald:wght@300;400&family=Roboto:wght@400;500;700&display=swap" rel="stylesheet">
<style>
:root{
  --green:#7fd62a;
  --green-dark:#5cb31a;
  --ink:#2b2b2b;
  --muted:#7a7a7a;
  --line:#e6e6e6;
  --grey-bg:#f3f3f3;
  --footer:#272a39;
  --footer-base:#1f2230;
  --white:#ffffff;
}
*{box-sizing:border-box;margin:0;padding:0}
html,body{width:1200px;height:2821px;overflow:hidden;background:var(--white)}
body{position:relative;font-family:'Roboto',sans-serif;color:var(--ink)}
.abs{position:absolute}
.heading{font-family:'Oswald',sans-serif;font-weight:300;color:var(--ink)}
.underline{display:block;width:50px;height:3px;background:linear-gradient(90deg,var(--green) 0 40%,transparent 40% 55%,#333 55%)}

/* header */
.social{top:27px;left:88px;display:flex;gap:10px}
.social span{width:28px;height:28px;border-radius:50%;background:var(--green-dark)}
.social span+span{background:#fff;border:1px solid #ccc}
.brand{top:20px;left:0;width:1200px;display:flex;justify-content:center;align-items:center;gap:8px}
.brand-mark{width:44px;height:44px;background:var(--green)}
.brand-name{font-size:28px;font-weight:700;color:#2e9a2a}
.call{top:22px;left:985px;display:flex;gap:10px;align-items:center}
.call small{display:block;font-size:12px;color:var(--muted)}
.call b{font-size:15px}
.nav{top:85px;left:88px;width:1024px;height:54px;background:var(--green);display:flex;align-items:center;justify-content:center;gap:36px;color:#fff;font-size:14px;z-index:3}
.nav .search{position:absolute;right:14px;top:13px;width:28px;height:28px;border-radius:50%;background:rgba(255,255,255,.25)}

/* hero */
.hero{top:113px;left:0;width:1200px;height:527px;background:linear-gradient(180deg,#3d4fc0 0%,#6d7fd8 40%,#b5a48a 70%,#4d6a2c 100%)}
.hero-text{top:280px;left:0;width:1200px;text-align:center;color:#fff}
.hero-text small{font-size:13px}
.hero-text h1{font-family:'Oswald',sans-serif;font-weight:400;font-size:46px;margin:4px 0 6px}
.hero-text p{font-size:13px;line-height:20px;width:440px;margin:0 auto}
.hero-btn{display:inline-block;margin-top:18px;border:1px solid #fff;padding:9px 20px;font-size:12px}
.arrow-btn{width:34px;height:34px;border-radius:50%;background:rgba(255,255,255,.85)}

/* about */
.about-title{top:706px;left:0;width:1200px;text-align:center;font-size:30px}
.about-img{top:786px;left:88px;width:508px;height:299px;background:linear-gradient(180deg,#6c9bd6,#c8d8ea 60%,#6b8a50)}
.about-img span{position:absolute;top:24px;left:18px;color:#fff;font-weight:700;font-size:18px}
.about-copy{top:796px;left:630px;width:480px;font-size:13px;line-height:21px;color:var(--muted)}
.ticks{list-style:none;margin-top:14px}
.ticks li{display:flex;gap:14px;align-items:center;height:40px;font-size:13px;color:#555}
.btn{display:inline-block;background:var(--green);color:#fff;font-size:12px;font-weight:500;padding:11px 22px;margin-top:12px}

/* services */
.services{top:1155px;left:0;width:1200px;height:410px;background:var(--grey-bg)}
.svc-title{top:1218px;left:88px;font-size:31px}
.svc-lead{top:1286px;left:88px;width:290px;font-size:13px;line-height:21px;color:var(--muted)}
.sensor{top:1345px;left:160px;width:122px;height:220px;background:linear-gradient(180deg,#9aa0a6,#5e646a 40%,#6b6b5c)}
.card{width:312px;height:115px;background:#fff;box-shadow:0 3px 10px rgba(0,0,0,.06);padding:26px 50px 0 60px}
.card h3{font-size:13px;font-weight:500;margin-bottom:8px}
.card p{font-size:12px;line-height:19px;color:var(--muted)}
.card .ico{position:absolute;left:18px;top:26px}
.card .go{position:absolute;right:-12px;top:44px;width:28px;height:28px;background:#fff;box-shadow:0 1px 5px rgba(0,0,0,.15);display:flex;align-items:center;justify-content:center}

/* projects */
.proj-title{top:1628px;left:0;width:1200px;text-align:center;font-size:30px}
.proj-cap{width:300px;height:150px;background:#fff;border:1px solid #eee}
.proj-cap .n{position:absolute;left:26px;top:104px;font-size:30px;font-weight:500;color:#ccc}
.proj-cap p{position:absolute;left:64px;top:106px;font-size:12px;line-height:18px;color:#666;width:200px}
.proj-img{width:297px;height:222px}

/* testimonials */
.testi-band{top:2075px;left:408px;width:792px;height:402px;background:var(--green)}
.quote-deco{top:2097px;left:0;width:165px;height:122px}
.testi-title{top:2255px;left:90px;font-size:32px}
.tcard{top:2161px;width:319px;height:232px;background:#fff;box-shadow:0 4px 14px rgba(0,0,0,.1);padding:30px 32px}
.person{display:flex;gap:14px;align-items:center;margin-bottom:28px}
.avatar{width:52px;height:52px;border-radius:50%;background:#9a9a9a}
.person b{font-size:13px;display:block}
.person small{font-size:11px;color:#999}
.tcard p{font-size:12px;line-height:22px;color:#555}

/* footer */
.footer{top:2477px;left:0;width:1200px;height:298px;background:var(--footer);color:#b8bac4;font-size:12px}
.footer-base{top:2775px;left:0;width:1200px;height:46px;background:var(--footer-base);color:#9a9ca6;font-size:12px;text-align:center;line-height:46px}
.f-col{position:absolute;top:50px}
.f-col h4{font-family:'Oswald',sans-serif;font-weight:300;font-size:17px;color:#fff;margin-bottom:24px}
.f-col li{list-style:none;line-height:27px}
.f-col li::before{content:"›";margin-right:8px}
.contact div{display:flex;gap:12px;margin-bottom:14px;line-height:18px}
.to-top{top:2758px;left:1140px;width:34px;height:30px;background:var(--green)}
</style>
</head>
<body>

<header>
  <div class="abs social"><span></span><span></span><span></span></div>
  <div class="abs brand"><span class="brand-mark"></span><span class="brand-name">Lindqvist Messtechnik</span></div>
  <div class="abs call">
    <svg width="22" height="34" viewBox="0 0 22 34"><rect x="2" y="2" width="18" height="30" rx="3" fill="none" stroke="#5cb31a" stroke-width="3"/><circle cx="11" cy="27" r="1.6" fill="#5cb31a"/></svg>
    <div><small>Call Us</small><b>+ 123 555 0147</b></div>
  </div>
  <nav class="abs nav">
    <svg width="14" height="12" viewBox="0 0 14 12"><path d="M7 0 14 6H12V12H8.5V8H5.5V12H2V6H0Z" fill="#fff"/></svg>
    <span>About Us</span><span>Our Services</span><span>Prices</span><span>Blog</span><span>Projects</span><span>Team</span><span>Contact Us</span>
    <span class="search"></span>
  </nav>
</header>

<section>
  <div class="abs hero" role="img" aria-label="City skyline with glass high-rise towers and green trees under a blue sky"></div>
  <svg class="abs" style="top:600px;left:0" width="1200" height="64" viewBox="0 0 1200 64"><path d="M0 40H480C540 40 550 62 600 62S660 40 720 40H1200V64H0Z" fill="#fff"/></svg>
  <svg class="abs" style="top:622px;left:590px" width="20" height="30" viewBox="0 0 20 30"><rect x="2" y="2" width="16" height="26" rx="8" fill="none" stroke="#888" stroke-width="2"/><rect x="9" y="8" width="2" height="6" fill="#888"/></svg>
  <div class="abs arrow-btn" style="top:377px;left:26px"></div>
  <div class="abs arrow-btn" style="top:377px;left:1140px"></div>
  <div class="abs hero-text">
    <small>Welcome To</small>
    <h1>Lindqvist Messtechnik</h1>
    <p>This is Photoshop's version of Lorem Ipsum. Proin gravida nibh velit auctor aliquet aenean sollici lorem quis bibendum auctor...</p>
    <span class="hero-btn">LEARN MORE</span>
  </div>
</section>

<section>
  <h2 class="abs heading about-title">About Us<span class="underline" style="margin:10px auto 0"></span></h2>
  <div class="abs about-img" role="img" aria-label="Modern glass office towers with a street and trees, video preview"><span>LINDQVIST MESSTECHNIK</span></div>
  <div class="abs about-copy">
    <p>This is Photoshop's version of Lorem Ipsum proin gravida nibh vel velit auctor aliquet aenean sollicitudin, lorem quis bibendum auctor, nisi elit consequat ipsum nec sagittis sem nibh id elit duis sed odio sit amet nibh vulputate cursus [...]</p>
    <ul class="ticks">
      <li><svg width="14" height="12"><path d="M1 6 5 10 13 1" fill="none" stroke="#ccc" stroke-width="2"/></svg>This is Photoshop's version of Lorem Ipsum proin gravida nibh</li>
      <li><svg width="14" height="12"><path d="M1 6 5 10 13 1" fill="none" stroke="#ccc" stroke-width="2"/></svg>Aenean sollicitudin, lorem quis bibendum auctor</li>
      <li><svg width="14" height="12"><path d="M1 6 5 10 13 1" fill="none" stroke="#ccc" stroke-width="2"/></svg>Nisi elit consequat ipsum nec elit.</li>
      <li><svg width="14" height="12"><path d="M1 6 5 10 13 1" fill="none" stroke="#ccc" stroke-width="2"/></svg>Duis sed odio sit amet nibh vulputate cursus a sit amet mauris.</li>
    </ul>
    <span class="btn">LEARN MORE</span>
  </div>
</section>

<section>
  <div class="abs services"></div>
  <h2 class="abs heading svc-title">Our Services<span class="underline" style="margin-top:10px"></span></h2>
  <p class="abs svc-lead">This is Photoshop's version of Lorem Ipsum proin gravida nibhvelit auctor aliquet aenean...</p>
  <div class="abs sensor" role="img" aria-label="Temperature sensor with metal connection head and long probe"></div>

  <div class="abs card" style="top:1228px;left:425px">
    <svg class="ico" width="30" height="30" viewBox="0 0 30 30"><circle cx="15" cy="15" r="11" fill="none" stroke="#7fd62a" stroke-width="2.5"/><path d="M15 8V15H21" stroke="#7fd62a" stroke-width="2.5" fill="none"/></svg>
    <h3>LOREM IPSUM IS SIMPLY...</h3><p>This is Photoshop's version of Lorem Ipsum proin gravida nibh vel...</p>
    <span class="go"><svg width="8" height="10"><path d="M2 1 6 5 2 9" fill="none" stroke="#333" stroke-width="1.6"/></svg></span>
  </div>
  <div class="abs card" style="top:1228px;left:779px">
    <svg class="ico" width="30" height="30" viewBox="0 0 30 30"><rect x="3" y="3" width="24" height="24" fill="none" stroke="#7fd62a" stroke-width="2.5"/><path d="M9 20V12M15 20V8M21 20V14" stroke="#7fd62a" stroke-width="2.5"/></svg>
    <h3>LOREM IPSUM IS SIMPLY...</h3><p>This is Photoshop's version of Lorem Ipsum proin gravida nibh vel...</p>
    <span class="go"><svg width="8" height="10"><path d="M2 1 6 5 2 9" fill="none" stroke="#333" stroke-width="1.6"/></svg></span>
  </div>
  <div class="abs card" style="top:1377px;left:425px">
    <svg class="ico" width="30" height="30" viewBox="0 0 30 30"><rect x="3" y="5" width="24" height="20" fill="none" stroke="#7fd62a" stroke-width="2.5"/><path d="M8 12H22M8 18H17" stroke="#7fd62a" stroke-width="2.5"/></svg>
    <h3>LOREM IPSUM IS SIMPLY...</h3><p>This is Photoshop's version of Lorem Ipsum proin gravida nibh vel...</p>
    <span class="go"><svg width="8" height="10"><path d="M2 1 6 5 2 9" fill="none" stroke="#333" stroke-width="1.6"/></svg></span>
  </div>
  <div class="abs card" style="top:1377px;left:779px">
    <svg class="ico" width="30" height="30" viewBox="0 0 30 30"><path d="M5 5 25 25M25 5 5 25" stroke="#7fd62a" stroke-width="2.5"/><circle cx="15" cy="15" r="4" fill="#fff" stroke="#7fd62a" stroke-width="2.5"/></svg>
    <h3>LOREM IPSUM IS SIMPLY...</h3><p>This is Photoshop's version of Lorem Ipsum proin gravida nibh vel...</p>
    <span class="go"><svg width="8" height="10"><path d="M2 1 6 5 2 9" fill="none" stroke="#333" stroke-width="1.6"/></svg></span>
  </div>
</section>

<section>
  <h2 class="abs heading proj-title">Our Projects<span class="underline" style="margin:10px auto 0"></span></h2>
  <div class="abs proj-cap" style="top:1853px;left:118px"><span class="n">1</span><p>Aenean vulputate eleifend dec ips tellus.</p></div>
  <div class="abs proj-cap" style="top:1853px;left:466px"><span class="n" style="color:var(--green)">2</span><p>Aenean vulputate eleifend dec ips tellus.</p></div>
  <div class="abs proj-cap" style="top:1853px;left:816px"><span class="n">3</span><p>Aenean vulputate eleifend dec ips tellus.</p></div>
  <div class="abs proj-img" style="top:1714px;left:88px;background:linear-gradient(160deg,#1e4fa0,#6aa2e0 60%,#cfe2f7)" role="img" aria-label="Blue glass skyscraper seen from below"></div>
  <div class="abs proj-img" style="top:1714px;left:437px;background:linear-gradient(180deg,#9cb4d0,#8a7a6a 50%,#3e6a2a)" role="img" aria-label="City street lined with tall buildings and trees"></div>
  <div class="abs proj-img" style="top:1714px;left:786px;background:linear-gradient(180deg,#a9c8e6,#9aa8a8 45%,#3f7a2c)" role="img" aria-label="Green park with city towers in the distance"></div>
</section>

<section>
  <div class="abs testi-band"></div>
  <svg class="abs quote-deco" viewBox="0 0 165 122"><path d="M0 0H70V60L40 122H10L30 70H0ZM95 0H165V60L135 122H105L125 70H95Z" fill="#efefef"/></svg>
  <h2 class="abs heading testi-title">Testimonial<span class="underline" style="margin-top:10px"></span></h2>

  <div class="abs tcard" style="left:292px">
    <div class="person"><span class="avatar" role="img" aria-label="Client portrait"></span><div><b>Ana Ruiz</b><small>@ana</small></div></div>
    <p>Aenean vulputate eleifend tellus aenean leo ligula porttitor eu, consequat vitae eleifend ac enim aliquam lorem ante dapibus in viverra quis feugiat a tellus.</p>
  </div>
  <div class="abs tcard" style="left:640px">
    <div class="person"><span class="avatar" role="img" aria-label="Client portrait"></span><div><b>Mark Olsen</b><small>@markolsen</small></div></div>
    <p>Aenean vulputate eleifend tellus aenean leo ligula porttitor eu, consequat vitae eleifend ac enim aliquam lorem ante dapibus in viverra quis feugiat a tellus.</p>
  </div>
  <div class="abs tcard" style="left:986px">
    <div class="person"><span class="avatar" role="img" aria-label="Client portrait"></span><div><b>Peter Hale</b><small>@peter</small></div></div>
    <p>Aenean vulputate eleifend tellus aenean leo ligula porttitor eu, consequat vitae eleifend ac enim aliquam lorem ante dapibus in viverra quis feugiat a tellus.</p>
  </div>
</section>

<footer>
  <div class="abs footer">
    <div class="f-col" style="left:88px;top:55px;width:210px">
      <div style="display:flex;align-items:center;gap:8px;margin-bottom:30px"><span style="width:30px;height:30px;background:var(--green)"></span><span style="font-size:15px;font-weight:700;color:#fff">Lindqvist Messtechnik</span></div>
      <p style="line-height:20px">This is Photoshop's version of Lorem Ipsum proin gravida nibhvelit auctor aliquet aenean...</p>
      <div style="display:flex;gap:10px;margin-top:16px"><span style="width:28px;height:28px;border-radius:50%;background:#fff"></span><span style="width:28px;height:28px;border-radius:50%;background:#3a3d4d"></span><span style="width:28px;height:28px;border-radius:50%;background:#3a3d4d"></span></div>
    </div>
    <div class="f-col" style="left:378px">
      <h4>Information</h4>
      <ul><li>Home</li><li>About Us</li><li>Our Services</li><li>Prices</li><li>Blog</li><li>Projects Team</li></ul>
    </div>
    <div class="f-col contact" style="left:564px;width:200px">
      <h4>Contact info</h4>
      <div><svg width="10" height="14"><path d="M5 0A5 5 0 0 1 10 5C10 9 5 14 5 14S0 9 0 5A5 5 0 0 1 5 0Z" fill="#7fd62a"/></svg><span>lindqvist messtechnik, City name goes here, / Country name.</span></div>
      <div><svg width="12" height="12"><path d="M2 0H5L6 3 4 5C5 7 6 8 8 8L9 6 12 7V10C12 11 11 12 10 12 4 12 0 8 0 2 0 1 1 0 2 0Z" fill="#7fd62a"/></svg><span>+123 555 0147</span></div>
      <div><svg width="14" height="10"><rect x="1" y="1" width="12" height="8" fill="none" stroke="#7fd62a" stroke-width="1.5"/><path d="M1 1 7 6 13 1" fill="none" stroke="#7fd62a" stroke-width="1.5"/></svg><span>info@lindqvist-mt.com</span></div>
    </div>
    <div class="f-col" style="left:880px;width:232px">
      <h4>Newsletter signup</h4>
      <p>Subscribe to our newsletter for updates.</p>
      <div style="display:flex;align-items:center;gap:10px;margin-top:20px;padding-bottom:10px;border-bottom:1px solid #4a4d5c;font-size:11px">
        <svg width="14" height="10"><rect x="1" y="1" width="12" height="8" fill="none" stroke="#7fd62a" stroke-width="1.5"/></svg>
        <span style="flex:1">Enter email address</span>
        <svg width="12" height="10"><path d="M0 5H11M7 1 11 5 7 9" fill="none" stroke="#7fd62a" stroke-width="1.5"/></svg>
      </div>
    </div>
  </div>
  <div class="abs footer-base">© 2017, All Rights Reserved.</div>
  <div class="abs to-top"><svg width="34" height="30"><path d="M17 9V21M12 14 17 9 22 14" fill="none" stroke="#fff" stroke-width="2"/></svg></div>
</footer>

</body>
</html>
```